Redesign cement bags for leading cement producer in south east asia

We are from Talvero cement and would like to redesign our bag to relaunch the product line. Our bags are made of high quality PP woven sack. We are one of the leading cement producers and we want our bags to have a Talvero classy look on each visible side when it is loading in a truck or stacking on a pallet.

Thank you for interesting in this project. Good luck.
Updates

Project Deadline Extended Reason: Hi all, I have received requests to extend the deadline. Some of the work requires revising and some of them are still on process. To be fair, I also raise my budget to compensate the time. Thanks all for your participation. Added Sunday, July 10, 2016

Target Market(s)

Construction

Industry/Entity Type

Cement

Requirements
Must have
• You will have to design two bags for two cement grades. 52.5 is of higher grade and 42.5 is of lower grade. Both are similar in design but a distinctive colours to differentiate the two at once. Please look at Reference picture 2 for ideas.
Nice to have
• You do not have to change the original logo but the Talvero cement word font changes are required. There are no restrictions to colours and font but please refrain from using feminine colours. Instructions on rear side of the bags are now included in the scope. Please create new layout and design new user friendly symbols.
Should not have
• Since cement is a dusty product, you need avoid some colours like black as background. The dust need to be less obvious to attract attention. Our previous base colour are shown in below.
• We want a fresh look on our bag, please do not just copy our old design and make small changes. I have attached our competitors' design, please refrain from using their design as well.
• It is recommend to do some research on cement bag sector.

```html
<!DOCTYPE html>
<html lang="en">
<head>
<meta charset="utf-8">
<title>Talvero Cement – 42.5 Bag Layout</title>
<link href="https://fonts.googleapis.com/css2?family=Rubik:wght@500;700;800&family=Titillium+Web:wght@300;400&family=Roboto:wght@500;700&display=swap" rel="stylesheet">
<style>
  :root {
    --paper: #e9e5d5;
    --ink: #1f2e37;
    --paper-text: #ece8d8;
  }
  /* Grade themes: 42.5 uses deep slate; 52.5 uses deep forest green */
  .bag--grade-42 { --ink: #1f2e37; }
  .bag--grade-52 { --ink: #1f4a3a; }

  html, body { margin: 0; padding: 0; overflow: hidden; background: var(--paper); }
  .bag {
    position: relative; width: 1200px; height: 961px; overflow: hidden;
    background: var(--paper); color: var(--ink);
    font-family: "Titillium Web", sans-serif;
  }
  .bag > * { position: absolute; margin: 0; }
  .artwork { left: 0; top: 0; }
  sup { font-size: 6px; line-height: 0; vertical-align: 4px; }

  .flip-headline {
    left: 40px; top: 44px; width: 520px; text-align: center;
    transform: rotate(180deg);
    font-family: "Rubik", sans-serif; font-weight: 800; font-size: 31px; line-height: 1; letter-spacing: 0.3px;
    white-space: nowrap;
  }

  .brand-name {
    left: 10px; top: 208px; width: 530px; text-align: center;
    font-family: "Rubik", sans-serif; font-weight: 800; font-size: 104px; line-height: 1; letter-spacing: -3px;
  }
  .brand-sub {
    left: 90px; top: 330px; width: 330px; text-align: center;
    font-weight: 300; font-size: 56px; letter-spacing: 0.15em; line-height: 1; padding-left: 0.15em;
  }
  .grade-pill {
    left: 138px; top: 448px; width: 228px; height: 30px; border-radius: 15px;
    background: var(--ink); color: var(--paper-text);
    font-family: "Rubik", sans-serif; font-weight: 700; font-size: 13px; letter-spacing: 1.2px;
    display: flex; align-items: center; justify-content: center;
  }
  .grade-type {
    left: 110px; top: 481px; width: 284px; text-align: center;
    font-weight: 300; font-size: 22px; letter-spacing: 0.12em; line-height: 1.3;
  }
  .origin {
    left: 80px; top: 759px; width: 344px; text-align: center; color: var(--paper-text);
    font-weight: 300; font-size: 21px; letter-spacing: 0.1em;
  }
  .net-weight {
    left: 80px; top: 800px; width: 344px; text-align: center; color: var(--paper-text);
    font-family: "Rubik", sans-serif; font-weight: 800; font-size: 19px; letter-spacing: -0.5px;
  }

  .side-band { top: 118px; width: 96px; height: 724px; background: var(--ink); color: var(--paper-text); }
  .side-band--front { left: 504px; }
  .side-band--back { left: 1104px; }
  .side-band > * { position: absolute; left: 50%; }
  .band-word {
    writing-mode: vertical-rl; transform: translateX(-50%) rotate(180deg); white-space: nowrap; line-height: 1;
  }
  .band-word--thin { top: 128px; font-weight: 300; font-size: 50px; letter-spacing: 0.2em; }
  .band-word--bold { top: 462px; font-family: "Rubik", sans-serif; font-weight: 800; font-size: 44px; letter-spacing: -0.5px; }
  .band-star { width: 24px; height: 24px; transform: translateX(-50%); }
  .band-star--upper { top: 420px; }
  .band-star--lower { top: 682px; }

  .section-title {
    left: 640px; width: 400px; text-align: center; font-weight: 300; font-size: 28px; line-height: 1; letter-spacing: 0.2px;
  }
  .title-applications { top: 154px; }
  .title-mixing { top: 238px; }
  .title-recommend { top: 407px; }
  .applications-note { left: 640px; top: 191px; width: 400px; text-align: center; font-weight: 300; font-size: 13px; }

  .mix-table { left: 650px; top: 274px; width: 380px; height: 110px; font-weight: 300; font-size: 13px; }
  .mix-table span { position: absolute; white-space: nowrap; transform: translateX(-50%); }
  .mix-table svg { position: absolute; left: 0; top: 0; }

  .advice-list { left: 656px; top: 463px; width: 420px; padding: 0; list-style: none; }
  .advice-list li {
    display: flex; align-items: center; gap: 6px; height: 30.5px;
    font-weight: 300; font-size: 10px; line-height: 1.2; text-transform: uppercase; letter-spacing: -0.1px; white-space: nowrap;
  }
  .advice-list svg { flex: none; width: 24px; height: 24px; }

  .maker { left: 730px; top: 642px; width: 400px; font-family: "Roboto", sans-serif; font-weight: 700; }
  .maker-mark { position: absolute; left: 0; top: 0; width: 44px; height: 44px; }
  .maker-label { position: absolute; left: 51px; top: 3px; font-size: 11.5px; font-weight: 500; }
  .maker-name { position: absolute; left: 51px; top: 22px; font-size: 18px; white-space: nowrap; letter-spacing: -0.2px; }
  .maker-address {
    position: absolute; left: 51px; top: 50px; margin: 0; font-style: normal;
    font-size: 10px; line-height: 13.6px; white-space: nowrap;
  }
  .indent { padding-left: 28px; }
</style>
</head>
<body>
<main class="bag bag--grade-42">
  <svg class="artwork" width="1200" height="961" viewBox="0 0 1200 961" aria-hidden="true">
    <g stroke="var(--ink)" stroke-width="6" fill="none">
      <line x1="0" y1="472" x2="1200" y2="1011"/>
      <line x1="0" y1="512" x2="1200" y2="1051"/>
      <line x1="0" y1="548" x2="1200" y2="1087"/>
    </g>
    <polygon points="0,548 504,774 504,842 0,842" fill="var(--ink)"/>
  </svg>

  <div class="flip-headline">EXPORT QUALITY 42.5 CEMENT</div>

  <h1 class="brand-name">TALVERO</h1>
  <div class="brand-sub">CEMENT</div>
  <div class="grade-pill">STRENGTH CLASS 42.5</div>
  <div class="grade-type">PORTLAND CEMENT</div>
  <div class="origin">PRODUCT OF MYANMAR</div>
  <div class="net-weight">NET WEIGHT 50KG</div>

  <div class="side-band side-band--front">
    <div class="band-word band-word--thin">CEMENT</div>
    <svg class="band-star band-star--upper" viewBox="0 0 24 24"><polygon fill="var(--paper-text)" points="12,1 15,9 23,9 16.5,14 19,22 12,17 5,22 7.5,14 1,9 9,9"/></svg>
    <div class="band-word band-word--bold">TALVERO</div>
    <svg class="band-star band-star--lower" viewBox="0 0 24 24"><polygon fill="var(--paper-text)" points="12,1 15,9 23,9 16.5,14 19,22 12,17 5,22 7.5,14 1,9 9,9"/></svg>
  </div>

  <div class="side-band side-band--back">
    <div class="band-word band-word--thin">CEMENT</div>
    <div class="band-word band-word--bold">TALVERO</div>
  </div>

  <h2 class="section-title title-applications">APPLICATIONS</h2>
  <p class="applications-note">SUITABLE FOR GENERAL CONCRETE PRODUCTS</p>

  <h2 class="section-title title-mixing">MIXING INSTRUCTIONS</h2>
  <div class="mix-table">
    <span style="left:74px;top:0">APPLICATIONS</span>
    <span style="left:154px;top:0">CEMENT</span>
    <span style="left:211px;top:0">SAND</span>
    <span style="left:272px;top:0">AGGREGATE</span>
    <span style="left:344px;top:0">WATER</span>
    <span style="left:74px;top:38px">LEAN CONCRETE</span>
    <span style="left:74px;top:83px">GENERAL CONCRETE</span>
    <svg width="380" height="110" viewBox="0 0 380 110">
      <defs>
        <symbol id="pail" viewBox="0 0 12 12">
          <path d="M2 4 L10 4 L9 11 L3 11 Z M3.5 4 Q6 0 8.5 4" fill="none" stroke="var(--ink)" stroke-width="1"/>
        </symbol>
      </defs>
      <use href="#pail" x="152" y="41" width="11" height="11"/>
      <use href="#pail" x="198" y="27" width="11" height="11"/>
      <use href="#pail" x="198" y="41" width="11" height="11"/>
      <use href="#pail" x="211" y="41" width="11" height="11"/>
      <use href="#pail" x="260" y="24" width="11" height="11"/>
      <use href="#pail" x="260" y="37" width="11" height="11"/>
      <use href="#pail" x="273" y="37" width="11" height="11"/>
      <use href="#pail" x="260" y="51" width="11" height="11"/>
      <use href="#pail" x="273" y="51" width="11" height="11"/>
      <use href="#pail" x="331" y="41" width="11" height="11"/>
      <use href="#pail" x="152" y="79" width="11" height="11"/>
      <use href="#pail" x="198" y="79" width="11" height="11"/>
      <use href="#pail" x="210" y="79" width="11" height="11"/>
      <use href="#pail" x="260" y="75" width="11" height="11"/>
      <use href="#pail" x="273" y="75" width="11" height="11"/>
      <use href="#pail" x="260" y="88" width="11" height="11"/>
      <use href="#pail" x="273" y="88" width="11" height="11"/>
      <path d="M334 80 L331 80 L332 90 L334 90" fill="none" stroke="var(--ink)" stroke-width="1"/>
      <text x="340" y="89" font-family="Roboto, sans-serif" font-weight="700" font-size="9" fill="var(--ink)">or</text>
      <use href="#pail" x="353" y="79" width="11" height="11"/>
    </svg>
  </div>

  <h2 class="section-title title-recommend">RECOMMENDATIONS</h2>
  <ul class="advice-list">
    <li><svg viewBox="0 0 24 24"><circle cx="12" cy="12" r="12" fill="var(--ink)"/><path d="M8 17 L12 13 L11 8 M12 13 L16 16" stroke="var(--paper)" stroke-width="2" fill="none"/><circle cx="13" cy="6" r="1.8" fill="var(--paper)"/></svg><span>Lorem ipsum dolor sit amet, consectetur adipiscing elit, sed do eiusmod<br>tempor incididunt ut labore et dolore magna aliqua.</span></li>
    <li><svg viewBox="0 0 24 24"><circle cx="12" cy="12" r="12" fill="var(--ink)"/><path d="M8 13 V8 M10.5 12 V6 M13 12 V6.5 M15.5 13 V8 M8 13 Q8 18 12 18 Q16 18 16 13" stroke="var(--paper)" stroke-width="1.6" fill="none" stroke-linecap="round"/></svg><span>Lorem ipsum dolor sit amet, consectetur adipiscing elit, sed do eiusmod<br>tempor incididunt ut labore et dolore magna aliqua.</span></li>
    <li><svg viewBox="0 0 24 24"><circle cx="12" cy="12" r="12" fill="var(--ink)"/><circle cx="12" cy="12" r="6" fill="none" stroke="var(--paper)" stroke-width="1.6"/><line x1="6" y1="12" x2="18" y2="12" stroke="var(--paper)" stroke-width="1.6"/></svg><span>Lorem ipsum dolor sit amet, consectetur adipiscing elit, sed do eiusmod<br>tempor incididunt ut labore et dolore magna aliqua.</span></li>
    <li><svg viewBox="0 0 24 24"><circle cx="12" cy="12" r="12" fill="var(--ink)"/><rect x="7" y="7" width="10" height="10" rx="3" fill="none" stroke="var(--paper)" stroke-width="1.6"/><line x1="7" y1="12" x2="17" y2="12" stroke="var(--paper)" stroke-width="1.6"/></svg><span>Lorem ipsum dolor sit amet, consectetur adipiscing elit, sed do eiusmod<br>tempor incididunt ut labore et dolore magna aliqua.</span></li>
    <li><svg viewBox="0 0 24 24"><circle cx="12" cy="12" r="12" fill="var(--ink)"/><path d="M5 12 Q12 3 19 12 Z" fill="var(--paper)"/><path d="M12 12 V17 Q12 19 10 18" stroke="var(--paper)" stroke-width="1.5" fill="none"/></svg><span>Lorem ipsum dolor sit amet, consectetur adipiscing elit, sed do eiusmod<br>tempor incididunt ut labore et dolore magna aliqua.</span></li>
  </ul>

  <div class="maker">
    <svg class="maker-mark" viewBox="0 0 44 44" aria-hidden="true"><circle cx="22" cy="22" r="20" fill="var(--ink)"/></svg>
    <div class="maker-label">Manufactured and distributed by :</div>
    <div class="maker-name">SEIN TAW CEMENT CO.,LTD.</div>
    <address class="maker-address">
      No.48, 21<sup>st</sup> Street,<br>
      Between 62<sup>nd</sup> and 63<sup>rd</sup> Streets<br>
      Thiri Yadana Township<br>
      Mandalay , Myanmar<br>
      Tel : (95)2 41160 , (95)2 41172 , (95)2 55304<br>
      <span class="indent">(95)2 41185 , (95)2 57219 , (95)2 50436</span><br>
      Fax : (95)2 48817 , Email : info@seintawcement.example<br>
      www.seintawcement.example
    </address>
  </div>
</main>
</body>
</html>
```